Software Review & Lead Gen Website Needs a Design

We are starting a software lead generation company in the Appointment Reminder space. Our business model is very similar to toolpicker.net. We get paid when we introduce a qualified buyer to a software vendor by vetting out each buyer with a phone call with one of our experts.

The site needs to entice the buyer to call us or submit a form on our site for a quick interview where we will then narrow down the field of vendors to 3 that best suit their needs. Everything is 100% free for the buyer. We also provide reviews of each software vendor so that they can compare.

The website can currently be found at nudgerated.net (this is a mockup we have just been playing around with - we do not prefer this specific design look, although we do like the font style, icons and color styles)

We're looking for a design of the home page and of the review page (for the reviews, we are going to have a medical reviews page, a dental reviews page, vision reviews page and business reviews page - reminder software will vary depending on the category of the organization) about us, for vendors page, and how it works page.

We've attached some really basic mockups we created of each page in a PDF. Each page is labeled (some have a "2" and that just means as you scroll down) You definitely don't have to copy what we have - we've been told that its too "busy" looking. We feel that a professional web designer could do a much better job of simplifying the UI and creating a better flow as well as just making it more pleasing on the eyes.

For inspiration, see toolpicker.net (they have the exact same business model, but they work in multiple industries whereas we just work with reminder software) and quillhire.net (also a slightly similar model).

Feel free to use the text from our mockups, create your own, or just use latin and we can fill in the rest with what fits best in your design.

We have a logo that we can send you, but no photos, so please use your best judgement and we'll make changes as needed.

Most important to us:

- Strong, simple calls to action - we want the buyers to call us directly, download our buyer's guide (in exchange for their email) or fill out a form for us to call them - when we get them on the phone, we conduct a quick interview to assess their needs and then narrow down the vendors to just 3. The vendors then pay us for the introduction to the buyer.

- Conveys to the visitor how we can help them (narrow down their search, allow them to compare vendors, save time and avoid mistakes)

- Narrow down each visitor by the type of company they are (Medical, Dental, Vision or Business)

We like white space, and simple / modern looks.

Target Market(s)

Doctors offices, office managers and business people

Industry/Entity Type

Software

Font styles to use
Sans Serif

Colors
85abd2
33a6d7
33b7a4
f68d4d
f8ba93
aaaaaa
000000
cfcfcf

Requirements
Must have
• See description above
Nice to have
• We like the font ff-tisa-web-pro and can provide if necessary

```html
<!DOCTYPE html>
<html lang="en">
<head>
<meta charset="utf-8">
<title>Nudge Rated – Appointment Reminder Software Reviews</title>
<link rel="stylesheet" href="https://fonts.googleapis.com/css2?family=Open+Sans:ital,wght@0,400;0,600;0,700;1,400&display=swap">
<style>
:root{
  --black:#000000;
  --teal:#33b7a4;
  --orange:#f68d4d;
  --orange-light:#f8ba93;
  --blue:#33a6d7;
  --blue-soft:#85abd2;
  --grey:#aaaaaa;
  --grey-light:#cfcfcf;
  --grey-box:#c6c6c6;
  --white:#ffffff;
  --ink:#1a1a1a;
}
*{box-sizing:border-box;margin:0;padding:0}
html,body{width:1200px;height:2605px;overflow:hidden}
body{font-family:"Open Sans",Arial,sans-serif;color:var(--ink);background:var(--white);position:relative}
section,header,footer{position:relative;width:1200px}
.abs{position:absolute}
a{color:var(--blue);text-decoration:none}

/* header */
.site-header{height:76px;background:var(--black)}
.brand{left:125px;top:18px;color:var(--white);font-weight:700;font-size:24px;display:flex;align-items:center;gap:8px}
.brand-mark{width:26px;height:26px;border:2px solid var(--white)}
.main-nav{right:126px;top:26px;display:flex;font-size:15px;font-weight:600}
.main-nav a{color:var(--white);padding:0 16px;border-left:2px dotted var(--white)}
.main-nav a:first-child{border-left:none;color:var(--blue)}

/* hero */
.hero{height:372px;background:var(--teal);z-index:2}
.hero-title{left:205px;top:88px;color:var(--white);font-size:34px;font-weight:400}
.hero-sub{left:207px;top:132px;color:var(--white);font-size:15px;font-weight:700}
.hero-text{left:207px;top:158px;width:320px;color:var(--white);font-size:12px;line-height:21px}
.hero-screen{left:561px;top:32px;width:372px;height:248px;border-radius:8px;background:linear-gradient(180deg,#e9eef4,#c9d3de);border:10px solid #1c1c1c;border-bottom-width:14px}
.hero-base{left:540px;top:278px;width:414px;height:10px;background:#d7dde2;border-radius:0 0 8px 8px}
.slide-arrow{top:150px;width:62px;height:83px}
.slide-prev{left:0}
.slide-next{right:0}

/* call box */
.call-box{left:273px;top:313px;width:651px;height:110px;background:var(--grey-box);box-shadow:0 3px 6px rgba(0,0,0,.25);z-index:3}
.call-lead{left:19px;top:18px;width:330px;color:var(--white);font-size:15px;line-height:20px}
.call-phone{left:19px;top:60px;color:var(--white);font-size:21px;font-weight:700}
.btn{display:flex;align-items:center;justify-content:center;color:var(--white);font-weight:700}
.btn-consult{left:401px;top:31px;width:236px;height:47px;background:var(--blue);font-size:14px}

/* categories */
.categories{height:264px;background:var(--orange)}
.category{width:180px;text-align:center;color:var(--white);font-weight:600;font-size:15px;top:106px}
.category svg{display:block;margin:0 auto}
.category span{display:block;margin-top:28px}

/* testimonials */
.testimonials{height:254px;background:var(--grey)}
.section-title{width:100%;text-align:center;top:40px;color:var(--white);font-weight:700;font-size:15px}
.quote{top:86px;width:290px;color:var(--white);font-size:12px;line-height:22px}
.quote-by{top:200px;color:var(--white);font-size:14px;font-style:italic}
.quote-by b{font-weight:700}

/* showcase */
.showcase{height:288px;background:var(--grey-light)}
.tile-photo{top:41px;width:309px;height:169px}
.tile-btn{top:224px;width:150px;height:40px;font-size:11px;font-weight:600}
.tile-btn.analysis{background:var(--blue)}
.tile-btn.reviews{background:var(--orange)}

/* content */
.content{height:1074px;background:#f9f9f9}
.intro{left:125px;top:27px;width:627px;font-size:11px;line-height:22px}
.intro .note{margin-top:24px}
.guide-box{left:796px;top:28px;width:279px;height:417px;background:var(--grey)}
.guide-kicker{left:16px;top:13px;color:var(--white);font-weight:700;font-size:13px}
.guide-title{left:16px;top:44px;width:250px;color:var(--white);font-weight:700;font-size:14px;line-height:23px}
.guide-text{left:16px;top:98px;width:250px;color:var(--white);font-size:13.5px;line-height:22px}
.guide-photo{left:17px;top:174px;width:245px;height:168px}
.btn-guide{left:50px;top:358px;width:179px;height:40px;background:var(--orange);font-size:14px}

.lead-form{left:125px;top:486px;width:631px;height:539px;background:var(--blue)}
.form-title{top:26px;width:100%;text-align:center;color:var(--white);font-size:25px;font-weight:600;line-height:33px}
.form-pitch{left:20px;top:128px;width:250px;color:var(--white);font-weight:700;font-size:14px;line-height:24px}
.form-fields{left:280px;top:121px;width:309px;display:flex;flex-direction:column;gap:12px}
.field{height:36px;background:var(--white);border-radius:3px;font-size:12px;color:#444;display:flex;align-items:center;padding:0 12px;justify-content:space-between}
.form-legal{left:20px;top:474px;width:220px;color:var(--white);font-size:11px;line-height:18px}
.btn-submit{left:328px;top:478px;width:214px;height:40px;background:var(--orange);font-size:14px;border-radius:2px}

.report{left:794px;top:495px;width:282px}
.report-head{color:var(--teal);font-weight:700;font-size:14px;padding-bottom:12px;border-bottom:1px solid var(--grey-light)}
.report-item{margin-top:22px;font-size:14px;line-height:23px}
.report-item b{display:block}

/* footer */
.site-footer{height:277px;background:var(--black);color:var(--white);font-size:14px}
.foot-col{line-height:24px}
.foot-head{color:var(--blue);font-weight:700;margin-bottom:20px}
.social{left:141px;top:200px;display:flex;gap:6px}
.social span{width:32px;height:32px;border-radius:50%;background:var(--white)}
</style>
</head>
<body>

<header class="site-header">
  <div class="abs brand"><span class="brand-mark"></span>nudge rated</div>
  <nav class="abs main-nav"><a href="#">Reviews</a><a href="#">About Us</a><a href="#">Blog</a><a href="#">Contact Us</a></nav>
</header>

<section class="hero">
  <svg class="abs slide-arrow slide-prev" viewBox="0 0 62 83"><polygon points="0,0 42,0 62,41.5 42,83 0,83" fill="#e6e6e6"/><polyline points="33,30 22,41.5 33,53" fill="none" stroke="#aaaaaa" stroke-width="4"/></svg>
  <svg class="abs slide-arrow slide-next" viewBox="0 0 62 83"><polygon points="62,0 20,0 0,41.5 20,83 62,83" fill="#e6e6e6"/><polyline points="29,30 40,41.5 29,53" fill="none" stroke="#aaaaaa" stroke-width="4"/></svg>
  <h1 class="abs hero-title">The Authority On</h1>
  <div class="abs hero-sub">Appointment&nbsp; Reminder's Software</div>
  <p class="abs hero-text">Lorem Ipsum is simply dummy text of the printing and typesetting industry. Lorem Ipsum has been the industry's standard dummy text ever since the 1500s</p>
  <div class="abs hero-screen" role="img" aria-label="Laptop showing the review site home page"></div>
  <div class="abs hero-base"></div>
  <div class="abs call-box">
    <p class="abs call-lead">Well Help determine which patient reminder service is best for you</p>
    <p class="abs call-phone">Call us at 555-555-555</p>
    <a class="abs btn btn-consult" href="#">FREE CONSULTATION</a>
  </div>
</section>

<section class="categories">
  <div class="abs category" style="left:150px">
    <svg width="60" height="70" viewBox="0 0 60 70"><path d="M14 4c8 0 10 4 16 4s8-4 16-4c10 0 12 10 10 20-2 9-6 12-7 22-1 9-2 22-7 22-4 0-5-16-12-16s-8 16-12 16c-5 0-6-13-7-22C10 36 6 33 4 24 2 14 4 4 14 4z" fill="none" stroke="#fff" stroke-width="4"/></svg>
    <span>Dental</span>
  </div>
  <div class="abs category" style="left:391px">
    <svg width="60" height="70" viewBox="0 0 60 70"><rect x="20" y="8" width="20" height="10" fill="none" stroke="#fff" stroke-width="4"/><rect x="2" y="18" width="56" height="44" fill="#fff"/><rect x="25" y="28" width="10" height="26" fill="#f68d4d"/><rect x="17" y="36" width="26" height="10" fill="#f68d4d"/></svg>
    <span>Medical</span>
  </div>
  <div class="abs category" style="left:630px">
    <svg width="60" height="70" viewBox="0 0 60 70"><path d="M2 36C12 20 48 20 58 36 48 52 12 52 2 36z" fill="#fff"/><circle cx="30" cy="36" r="9" fill="#f68d4d"/></svg>
    <span>Vision</span>
  </div>
  <div class="abs category" style="left:868px">
    <svg width="60" height="70" viewBox="0 0 60 70"><path d="M4 8v56h54" fill="none" stroke="#fff" stroke-width="4"/><rect x="12" y="18" width="9" height="42" fill="#fff"/><rect x="25" y="30" width="9" height="30" fill="#fff"/><rect x="38" y="44" width="9" height="16" fill="#fff"/><rect x="50" y="50" width="6" height="10" fill="#fff"/></svg>
    <span>Business</span>
  </div>
</section>

<section class="testimonials">
  <h2 class="abs section-title">Testimonials</h2>
  <p class="abs quote" style="left:146px">Nudge Rated saved me so much time researching software, and the best part is they did it for free!</p>
  <p class="abs quote" style="left:466px">Thank you for helping me find a software that allows me to automatically remind our patients about their appointments with us. Very pleased with the service you provided.</p>
  <p class="abs quote" style="left:782px">I would have spent hours trying to find the right patient reminder software, but thanks to Nudge Rated, they did all the leg work for me.</p>
  <p class="abs quote-by" style="left:146px"><b>-Ben,</b> Brightline Dental</p>
  <p class="abs quote-by" style="left:466px"><b>-Sally,</b> Little Steps Pediatrics</p>
  <p class="abs quote-by" style="left:782px"><b>-Carl,</b> Westfield Clinic</p>
</section>

<section class="showcase">
  <div class="abs tile-photo" style="left:125px;background:radial-gradient(circle at 45% 50%,#bfe6fb,#2a8fd6 55%,#1460a8)" role="img" aria-label="Abstract blue data network"></div>
  <div class="abs tile-photo" style="left:445px;background:linear-gradient(135deg,#c9cdd0,#f2f2f2 50%,#b4b8bb)" role="img" aria-label="Hands joining puzzle pieces"></div>
  <div class="abs tile-photo" style="left:766px;background:linear-gradient(160deg,#d8e2ea,#6f8ea6 60%,#36536c)" role="img" aria-label="Hospital operating room equipment"></div>
  <a class="abs btn tile-btn analysis" style="left:125px" href="#">In Depth Analysis</a>
  <a class="abs btn tile-btn reviews" style="left:284px" href="#">User Reviews</a>
  <a class="abs btn tile-btn analysis" style="left:445px" href="#">In Depth Analysis</a>
  <a class="abs btn tile-btn reviews" style="left:604px" href="#">User Reviews</a>
  <a class="abs btn tile-btn analysis" style="left:766px" href="#">In Depth Analysis</a>
  <a class="abs btn tile-btn reviews" style="left:925px" href="#">User Reviews</a>
</section>

<section class="content">
  <div class="abs intro">
    <p>Lorem Ipsum is simply dummy text of the printing and typesetting industry. Lorem Ipsum has been the industry's standard dummy text ever since the 1500s, when an unknown printer took a galley of type and scrambled it to make a type specimen book. It has survived not only five centuries, but also the leap into electronic typesetting, remaining essentially unchanged.</p>
    <p>Lorem Ipsum is simply dummy text of the printing and typesetting industry. Lorem Ipsum has been the industry's standard dummy text ever since the 1500s, when an unknown printer took a galley of type and scrambled it to make a type specimen book. It has survived not only five centuries, but also the leap into electronic typesetting, remaining essentially unchanged.Lorem Ipsum is simply dummy text of the printing and typesetting industry. Lorem Ipsum has been the industry's standard dummy text ever since the 1500s, when an unknown printer took a galley of type and scrambled it to make a type specimen book. It has survived not only five centuries, but also the leap into electronic typesetting, remaining essentially unchanged.</p>
    <p>Lorem Ipsum is simply dummy text of the printing and typesetting industry. Lorem Ipsum has been the industry's standard dummy text ever since the 1500s, when an unknown printer took a galley of type and scrambled it to make a type specimen book. It has survived not only five centuries, but also the leap into electronic typesetting, remaining essentially unchanged.</p>
    <p class="note">Nudge Rated is a 100% Free Esrvice to help buyers find the best vendors that match their needs.Find out <a href="#">how it works</a> and <a href="#">Why its completely free</a> for buyers.</p>
  </div>

  <aside class="abs guide-box">
    <p class="abs guide-kicker">Free PDF Guide</p>
    <p class="abs guide-title">Ultimate Reminder Service Buyer's Guide</p>
    <p class="abs guide-text">The definitive guide to buying the perfect reminder software for your organization</p>
    <div class="abs guide-photo" style="background:linear-gradient(135deg,#e3eef7,#a9c4dc 60%,#6f93b4)" role="img" aria-label="Doctor holding a tablet"></div>
    <a class="abs btn btn-guide" href="#">GET BUYER'S GUIDE</a>
  </aside>

  <form class="abs lead-form">
    <h2 class="abs form-title">Get introduced to the top rated<br>reminder services in seconds</h2>
    <p class="abs form-pitch">We just need some basic oinfromation from you and well match you with the best of the best !<br>Get price quotes,product Demos + Our Free Buyers Guide without the hassle of trackingdown each vendor yourself.</p>
    <div class="abs form-fields">
      <div class="field">Your Company Name</div>
      <div class="field">First Name</div>
      <div class="field">Last Name</div>
      <div class="field">E-Mail</div>
      <div class="field">Phone</div>
      <div class="field" style="font-weight:600">Organisation Type<svg width="10" height="8" viewBox="0 0 10 8"><polygon points="0,0 10,0 5,8" fill="#222"/></svg></div>
      <div class="field">State</div>
    </div>
    <p class="abs form-legal">By clicking thebutton to the right you have read and agree to our terms of use and privacy policy</p>
    <a class="abs btn btn-submit" href="#">Show Me The Money !</a>
  </form>

  <aside class="abs report">
    <p class="report-head">Reminder Report</p>
    <p class="report-item"><b>Top % HIPAA Questions: Answered</b>See what our answers are to your top 5 HIPAA</p>
    <p class="report-item"><b>The Future of patient engagement equires a Look into the past</b></p>
    <p class="report-item">A trip down memmory lane leads us to an exiciting future in patient reminder software</p>
  </aside>
</section>

<footer class="site-footer">
  <div class="abs foot-col" style="left:141px;top:57px">Nudge Rated<br>© 2014 NudgeRated,Inc.</div>
  <div class="abs foot-col" style="left:141px;top:145px">Privacy Policy &nbsp;|&nbsp; Terms Of Use</div>
  <div class="abs social"><span role="img" aria-label="Social link"></span><span role="img" aria-label="Social link"></span><span role="img" aria-label="Social link"></span><span role="img" aria-label="Social link"></span></div>
  <div class="abs foot-col" style="left:457px;top:57px"><p class="foot-head">Who We Are</p>About Us<br>How It Works<br>Blog</div>
  <div class="abs foot-col" style="left:637px;top:57px"><p class="foot-head">For Vendors</p>Vendor Seal<br>Let's Connect</div>
  <div class="abs foot-col" style="left:767px;top:57px"><p class="foot-head">For Buyers</p>Medical<br>Dental<br>Vision<br>Business</div>
  <div class="abs foot-col" style="left:900px;top:57px"><p class="foot-head">Resources</p>Buyer's Guide<br>How We Grade<br>Contact Us</div>
  <div class="abs foot-col" style="left:767px;top:226px;color:var(--blue);font-weight:700">Free Advice</div>
  <div class="abs foot-col" style="left:900px;top:226px">P: 555-555-555</div>
</footer>

</body>
</html>
```